Letterhead Design for Law Firm that Specializes in Property Damage Litigation

We are looking for a redesign of our letterhead. Our current letterhead lists all of our current staff members and we'd like to come up with a design that does NOT list all of the staff members so that it does not need to be updated with every newly hired employee. Must be in editable format.

We are a law firm that specializes in property damage, so we need something that is professional, yet modern. The final design should use our existing logo and should use a blue color scheme (alternate colors would be gray, black, and white).

Industry/Entity Type

Legal

Colors
0054AA
0677BA
7BADD7
CADEEF
E8F1F8

```html
<!DOCTYPE html>
<html lang="en">
<head>
<meta charset="utf-8">
<title>Letterhead – Hartwell Crane &amp; Ostrander</title>
<link href="https://fonts.googleapis.com/css2?family=Arimo:wght@400;700&display=swap" rel="stylesheet">
<style>
  :root {
    --backdrop: #dcdcdc;
    --paper: #ffffff;
    --navy: #0b2c5f;
    --heading: #1b3070;
    --ink: #2b2b2b;
    --muted: #6b6b6b;
    --band-gray: #666666;
    --rule: #bdbdbd;
  }
  html, body {
    margin: 0;
    width: 1200px;
    height: 947px;
    overflow: hidden;
    background: var(--backdrop);
    font-family: "Arimo", Arial, sans-serif;
  }
  .letterhead {
    position: absolute;
    left: 364px;
    top: 179px;
    width: 472px;
    height: 606px;
    background: var(--paper);
  }
  .brand {
    position: absolute;
    left: 48px;
    top: 19px;
    width: 140px;
  }
  .brand-row {
    display: flex;
    align-items: center;
    gap: 6px;
  }
  .brand-square {
    width: 14px;
    height: 14px;
    background: var(--navy);
    flex: none;
  }
  .brand-name {
    color: var(--navy);
    font-weight: 700;
    font-size: 12.5px;
    line-height: 13.5px;
    letter-spacing: 0.6px;
    text-transform: uppercase;
  }
  .brand-tagline {
    margin-top: 7px;
    color: var(--muted);
    font-size: 5.2px;
    letter-spacing: 1.2px;
    text-transform: uppercase;
    white-space: nowrap;
  }
  .office {
    position: absolute;
    top: 15px;
    font-size: 8.4px;
    line-height: 10.3px;
    color: var(--ink);
  }
  .office-nj { left: 218px; }
  .office-pa { left: 329px; }
  .office h2 {
    margin: 0 0 3px;
    font-size: 8.6px;
    font-weight: 700;
    color: var(--heading);
    letter-spacing: 0.1px;
  }
  .office p { margin: 0; }
  .office b { color: var(--heading); }
  .office-divider {
    position: absolute;
    left: 318px;
    top: 17px;
    width: 1px;
    height: 61px;
    background: var(--rule);
  }
  .footer-band {
    position: absolute;
    left: 0;
    bottom: 0;
    width: 472px;
    height: 29px;
  }
  .footer-text {
    position: absolute;
    bottom: 8px;
    color: #ffffff;
    font-size: 9px;
  }
  .footer-phone { left: 128px; display: flex; align-items: center; gap: 4px; }
  .footer-web { left: 250px; }
</style>
</head>
<body>
  <main class="letterhead">
    <header>
      <div class="brand">
        <div class="brand-row">
          <span class="brand-square"></span>
          <div class="brand-name">Hartwell<br>Crane &amp;<br>Ostrander</div>
        </div>
        <div class="brand-tagline">The Property Damage Attorneys</div>
      </div>

      <section class="office office-nj">
        <h2>NEW JERSY OFFICE</h2>
        <p><b>P:</b> 856.555.0142</p>
        <p><b>F:</b> 215.555.0190</p>
        <p>2250 Mercer Road<br>North, Suite 310<br>Maple Ridge, NJ 08021</p>
      </section>
      <div class="office-divider"></div>
      <section class="office office-pa">
        <h2>PHILADELPHIA OFFICE</h2>
        <p><b>P:</b> 215.555.0100</p>
        <p><b>F:</b> 215.555.0190</p>
        <p>1800 Arch Lane<br>Suite 940<br>Philadelphia, PA 19107</p>
      </section>
    </header>

    <footer>
      <svg class="footer-band" viewBox="0 0 472 29" aria-hidden="true">
        <polygon points="0,0 234,0 222,29 0,29" fill="var(--band-gray)"/>
        <polygon points="238,0 472,0 472,29 227,29" fill="var(--navy)"/>
      </svg>
      <div class="footer-text footer-phone">
        <svg width="8" height="8" viewBox="0 0 24 24" aria-hidden="true">
          <path d="M6.6 10.8a15.1 15.1 0 0 0 6.6 6.6l2.2-2.2a1 1 0 0 1 1-.25 11.4 11.4 0 0 0 3.6.57 1 1 0 0 1 1 1V20a1 1 0 0 1-1 1A17 17 0 0 1 3 4a1 1 0 0 1 1-1h3.5a1 1 0 0 1 1 1c0 1.25.2 2.45.57 3.57a1 1 0 0 1-.25 1z" fill="none" stroke="#ffffff" stroke-width="2"/>
        </svg>
        <span>(215) 555-0100</span>
      </div>
      <div class="footer-text footer-web">www.hcolegal.com</div>
    </footer>
  </main>
</body>
</html>
```